Brackwell Immigration Law

We need a web design for our existing company www.brackwellcounsel.co.uk. We are an immigration consultancy. The final design should communicate professionalism, integrity and affordability.

Industry/Entity Type

It Company

Logo Text

Brackwell Counsel Partners

Number of Pages Required

5+ page

Font styles to use
Serif

Requirements
Must have
• I want to have the same silhouette logo but something different in positioning..
Nice to have
• Please have a look at these websites:
• https://www.travelpathguide.co.uk/visa_uk/
• http://www.oakdenadvisers.co.uk/
• http://www.myrtlegatelaw.org/index.php
• www.brackwellcounsel.co.uk

```html
<!DOCTYPE html>
<html lang="en">
<head>
<meta charset="UTF-8">
<title>Brackwell Counsel Partners – Immigration Law</title>
<link href="https://fonts.googleapis.com/css2?family=Lora:wght@400;700&family=Open+Sans:wght@400;600;700&display=swap" rel="stylesheet">
<style>
:root{
  --red:#a3141c;
  --red-dark:#7d0d13;
  --red-deep:#5c080d;
  --ink:#2b2b2b;
  --muted:#6b6b6b;
  --line:#dcdcdc;
  --paper:#ffffff;
  --soft:#f3f3f3;
  --serif:'Lora', Georgia, serif;
  --sans:'Open Sans', Arial, sans-serif;
}
*{box-sizing:border-box;margin:0;padding:0}
html,body{width:870px;height:1200px;overflow:hidden}
body{font-family:var(--sans);color:var(--ink);background:var(--paper);position:relative}

/* header */
.site-header{height:84px;display:flex;align-items:flex-start;justify-content:space-between;padding:10px 24px 0 28px;border-bottom:1px solid var(--line)}
.brand{display:flex;align-items:center;gap:10px;margin-top:4px}
.brand-mark{width:34px;height:34px;border-radius:50%;background:var(--red);flex-shrink:0}
.brand-name{font-family:var(--serif);font-weight:700;font-size:17px;line-height:1.1;color:var(--red)}
.main-nav{display:flex;align-self:flex-end;margin-bottom:12px;gap:2px}
.main-nav a{font-size:10px;font-weight:600;text-decoration:none;color:var(--ink);padding:6px 11px;text-transform:uppercase;letter-spacing:.3px}
.main-nav a.active{background:var(--red);color:#fff}
.header-contact{display:flex;flex-direction:column;align-items:flex-end;gap:5px}
.social-row{display:flex;gap:4px}
.social-row span{width:15px;height:15px;background:var(--red);display:block}
.call-line{display:flex;align-items:center;gap:6px;font-size:9px;color:var(--muted);text-align:right;line-height:1.2}
.call-line strong{display:block;font-size:13px;color:var(--red)}
.btn-callback{background:var(--red);color:#fff;font-size:9px;font-weight:700;padding:6px 10px;text-transform:uppercase}

/* visa band */
.visa-band{height:168px;background:linear-gradient(var(--red),var(--red-dark));display:flex;justify-content:space-around;align-items:flex-start;padding:22px 20px 0}
.visa-item{width:120px;text-align:center;color:#fff;font-size:10px;line-height:1.35}
.visa-icon{width:70px;height:70px;border-radius:50%;background:#fff;margin:0 auto 10px;display:flex;align-items:center;justify-content:center;border:3px solid rgba(255,255,255,.5);box-shadow:0 0 0 3px var(--red-dark)}

/* hero */
.hero{position:relative;height:338px;background:linear-gradient(110deg,#c7ccd6 0%,#8e9bb7 22%,#b2323c 48%,#d9d2cb 70%,#2c3f77 100%)}
.hero-caption{position:absolute;left:0;right:0;bottom:40px;text-align:center;font-family:var(--serif);font-size:30px;color:#fff;letter-spacing:1px;text-shadow:0 2px 4px rgba(0,0,0,.4)}
.hero-arrow{position:absolute;top:150px;width:22px;height:36px;background:rgba(40,40,40,.75);display:flex;align-items:center;justify-content:center}
.hero-arrow.prev{left:0}.hero-arrow.next{right:0}

/* about */
.about{height:240px;overflow:hidden;display:flex;gap:18px;padding:18px 24px 0}
.about-text{width:330px}
.section-title{font-family:var(--serif);font-size:18px;font-weight:700;color:var(--ink);padding-bottom:6px;border-bottom:2px solid var(--red);display:inline-block;margin-bottom:10px}
.about-text p{font-size:9.5px;line-height:1.55;color:var(--muted);margin-bottom:8px}
.btn-more{display:inline-block;background:var(--red);color:#fff;font-size:9px;font-weight:700;padding:5px 12px;margin-top:2px}
.about-video{width:180px}
.video-frame{height:132px;background:linear-gradient(135deg,#4e4a48,#8c7d72 55%,#2f2d2c);display:flex;align-items:center;justify-content:center}
.video-bar{height:14px;background:#222}
.about-services{flex:1;display:flex;flex-direction:column;gap:6px}
.tile-grid{display:grid;grid-template-columns:1fr 1fr;gap:6px}
.tile{background:var(--red);color:#fff;height:56px;display:flex;flex-direction:column;align-items:center;justify-content:center;gap:4px;font-size:9px;font-weight:600;text-align:center}
.tile.dark{background:var(--red-dark)}
.expert-banner{height:44px;background:linear-gradient(90deg,#d8d8d8,#b9b9b9);display:flex;align-items:center;padding-left:12px;font-family:var(--serif);font-size:11px;color:#fff;text-transform:uppercase;line-height:1.25;font-weight:700}

/* news + reviews */
.updates{height:190px;overflow:hidden;display:flex;gap:24px;padding:10px 24px 0;border-top:1px solid var(--line)}
.updates > section{flex:1}
.block-head{display:flex;align-items:center;gap:8px;font-family:var(--serif);font-weight:700;font-size:13px;text-transform:uppercase;padding-bottom:6px;border-bottom:1px solid var(--line);margin-bottom:10px}
.head-dot{width:18px;height:18px;border-radius:50%;background:var(--red);display:flex;align-items:center;justify-content:center}
.news-item{display:flex;gap:10px;margin-bottom:10px}
.news-date{width:36px;height:36px;background:var(--red);color:#fff;text-align:center;font-size:7px;line-height:1.1;padding-top:4px;flex-shrink:0}
.news-date b{display:block;font-size:14px}
.news-item h4{font-size:10px;color:var(--red);font-weight:700}
.news-item p{font-size:8.5px;color:var(--muted);line-height:1.4}
.review{display:flex;gap:8px}
.quote-mark{font-family:var(--serif);font-size:34px;line-height:.8;color:var(--red)}
.review p{font-size:9.5px;line-height:1.6;color:var(--muted);font-style:italic}
.reviewer{display:flex;align-items:center;gap:10px;margin:14px 0 0 24px;font-size:10px;font-weight:600}
.avatar{width:38px;height:38px;border-radius:50%;background:linear-gradient(#c9b7a6,#6d5d54)}

/* footer */
.site-footer{height:155px;overflow:hidden;background:var(--red-dark);color:#fff;display:flex;gap:26px;padding:14px 24px 0}
.footer-col h5{font-family:var(--serif);font-size:11px;font-weight:700;margin-bottom:6px}
.footer-col ul{list-style:none;font-size:8.5px;line-height:1.5}
.footer-col ul li::before{content:"› "}
.footer-col p{font-size:8.5px;line-height:1.45;margin-bottom:3px}
.enquiry{width:280px}
.enquiry-grid{display:grid;grid-template-columns:1fr 1fr;gap:4px;margin-top:4px}
.enquiry-grid span{height:14px;background:#fff;display:block}
.enquiry-grid span.wide{grid-column:1/3}
.btn-send{display:inline-block;border:1px solid #fff;font-size:8px;font-weight:700;padding:3px 8px;margin-top:6px}
.footer-brand{margin-left:auto;display:flex;align-items:center;gap:8px;align-self:center;margin-bottom:16px}
.footer-brand .brand-mark{background:#fff}
.footer-brand .brand-name{color:#fff}
.copyright{height:25px;background:var(--red-deep);color:#f0d9da;font-size:8.5px;display:flex;align-items:center;padding-left:24px}
</style>
</head>
<body>

<header class="site-header">
  <div class="brand">
    <span class="brand-mark"></span>
    <span class="brand-name">Brackwell<br>Counsel Partners</span>
  </div>
  <nav class="main-nav">
    <a href="#" class="active">Home</a>
    <a href="#">About Us</a>
    <a href="#">Services</a>
    <a href="#">News</a>
    <a href="#">Testimonials</a>
    <a href="#">Contact Us</a>
  </nav>
  <div class="header-contact">
    <div class="social-row"><span></span><span></span><span></span><span></span></div>
    <div class="call-line">
      <svg width="14" height="14" viewBox="0 0 24 24"><path fill="#a3141c" d="M6.6 10.8a15 15 0 006.6 6.6l2.2-2.2c.3-.3.7-.4 1-.2 1.1.4 2.3.6 3.6.6.6 0 1 .4 1 1V20c0 .6-.4 1-1 1A17 17 0 013 4c0-.6.4-1 1-1h3.5c.6 0 1 .4 1 1 0 1.3.2 2.5.6 3.6.1.3 0 .7-.2 1z"/></svg>
      <div>Call Us Today<strong>123-456-7890</strong></div>
    </div>
    <div class="btn-callback">Request a Call Back</div>
  </div>
</header>

<section class="visa-band">
  <div class="visa-item">
    <div class="visa-icon"><svg width="36" height="30" viewBox="0 0 36 30"><circle cx="13" cy="17" r="9" fill="none" stroke="#a3141c" stroke-width="3"/><circle cx="23" cy="17" r="9" fill="none" stroke="#a3141c" stroke-width="3"/></svg></div>
    Marriage, Fiancé<br>Relationship Visa
  </div>
  <div class="visa-item">
    <div class="visa-icon"><svg width="34" height="30" viewBox="0 0 34 30"><rect x="2" y="8" width="30" height="20" rx="2" fill="#a3141c"/><rect x="11" y="3" width="12" height="7" fill="none" stroke="#a3141c" stroke-width="3"/></svg></div>
    Work Visa
  </div>
  <div class="visa-item">
    <div class="visa-icon"><svg width="34" height="32" viewBox="0 0 34 32"><circle cx="10" cy="7" r="5" fill="#a3141c"/><circle cx="24" cy="9" r="4" fill="#a3141c"/><path d="M2 30c0-9 4-13 8-13s8 4 8 13zM17 30c0-7 3-11 7-11s7 4 7 11z" fill="#a3141c"/></svg></div>
    Adult Dependent<br>Relatives Visa
  </div>
  <div class="visa-item">
    <div class="visa-icon"><svg width="32" height="32" viewBox="0 0 32 32"><path d="M3 18l26-12-8 22-5-8z" fill="#a3141c"/></svg></div>
    Visiting Visa
  </div>
  <div class="visa-item">
    <div class="visa-icon"><svg width="32" height="28" viewBox="0 0 32 28"><path d="M3 15l9 9L29 4" fill="none" stroke="#a3141c" stroke-width="5"/></svg></div>
    Indefinite Leave<br>To Remain
  </div>
  <div class="visa-item">
    <div class="visa-icon"><svg width="30" height="32" viewBox="0 0 30 32"><rect x="4" y="2" width="3" height="28" fill="#a3141c"/><path d="M7 3h19l-4 7 4 7H7z" fill="#a3141c"/></svg></div>
    British<br>Citizenship
  </div>
</section>

<section class="hero" role="img" aria-label="Photo of smiling students holding books in front of a Union flag">
  <div class="hero-arrow prev"><svg width="10" height="14" viewBox="0 0 10 14"><path d="M8 1L2 7l6 6" fill="none" stroke="#fff" stroke-width="2"/></svg></div>
  <div class="hero-arrow next"><svg width="10" height="14" viewBox="0 0 10 14"><path d="M2 1l6 6-6 6" fill="none" stroke="#fff" stroke-width="2"/></svg></div>
  <div class="hero-caption">TO STUDY IN UK</div>
</section>

<section class="about">
  <div class="about-text">
    <h2 class="section-title">About Brackwell Counsel Partners</h2>
    <p>Lorem ipsum dolor sit amet, consectetuer adipiscing elit, sed diam nonummy nibh euismod tincidunt ut laoreet dolore magna aliquam erat volutpat. Ut wisi enim ad minim veniam, quis nostrud exerci tation ullamcorper suscipit lobortis nisl ut aliquip ex ea commodo consequat.</p>
    <p>Duis autem vel eum iriure dolor in hendrerit in vulputate velit esse molestie consequat, vel illum dolore eu feugiat nulla facilisis at vero eros et accumsan et iusto odio dignissim qui blandit praesent luptatum zzril delenit augue duis dolore.</p>
    <span class="btn-more">Read More</span>
  </div>
  <div class="about-video">
    <div class="video-frame" role="img" aria-label="Video still of legal advisers meeting a client">
      <svg width="34" height="24" viewBox="0 0 34 24"><rect width="34" height="24" rx="6" fill="#a3141c"/><path d="M13 7l9 5-9 5z" fill="#fff"/></svg>
    </div>
    <div class="video-bar"></div>
  </div>
  <div class="about-services">
    <div class="tile-grid">
      <div class="tile"><svg width="16" height="16" viewBox="0 0 16 16"><rect x="1" y="3" width="14" height="12" fill="none" stroke="#fff" stroke-width="1.6"/><path d="M1 7h14M5 1v4M11 1v4" stroke="#fff" stroke-width="1.6"/></svg>Open Day Service</div>
      <div class="tile dark"><svg width="16" height="16" viewBox="0 0 16 16"><circle cx="8" cy="8" r="6.5" fill="none" stroke="#fff" stroke-width="1.6"/><path d="M8 4v4l3 2" fill="none" stroke="#fff" stroke-width="1.6"/></svg>Weekend Service</div>
      <div class="tile dark"><svg width="18" height="14" viewBox="0 0 18 14"><rect x="1" y="1" width="16" height="12" fill="none" stroke="#fff" stroke-width="1.6"/><path d="M1 1l8 7 8-7" fill="none" stroke="#fff" stroke-width="1.6"/></svg>Sign up for Newsletter</div>
      <div class="tile"><svg width="16" height="16" viewBox="0 0 16 16"><path d="M8 1v9M4 6l4 4 4-4M2 14h12" fill="none" stroke="#fff" stroke-width="1.8"/></svg>Download Brochure</div>
    </div>
    <div class="expert-banner">Let our legal experts<br>help you</div>
  </div>
</section>

<section class="updates">
  <section>
    <div class="block-head"><span class="head-dot"><svg width="8" height="8" viewBox="0 0 8 8"><rect width="8" height="8" fill="#fff"/></svg></span>Latest News</div>
    <div class="news-item"><div class="news-date"><b>22</b>JAN</div><div><h4>Lorem ipsum dolor</h4><p>Lorem ipsum dolor sit amet, consectetuer adipiscing elit, sed diam nonummy nibh euismod tincidunt.</p></div></div>
    <div class="news-item"><div class="news-date"><b>23</b>JAN</div><div><h4>Lorem ipsum dolor</h4><p>Lorem ipsum dolor sit amet, consectetuer adipiscing elit, sed diam nonummy nibh euismod tincidunt.</p></div></div>
    <div class="news-item"><div class="news-date"><b>24</b>JAN</div><div><h4>Lorem ipsum dolor</h4><p>Lorem ipsum dolor sit amet, consectetuer adipiscing elit, sed diam nonummy nibh euismod tincidunt.</p></div></div>
  </section>
  <section>
    <div class="block-head"><span class="head-dot"><svg width="8" height="8" viewBox="0 0 8 8"><circle cx="4" cy="4" r="3.5" fill="#fff"/></svg></span>Customer Reviews</div>
    <div class="review">
      <span class="quote-mark">“</span>
      <p>Lorem ipsum dolor sit amet, sed diam nonummy nibh euismod tincidunt ut laoreet dolore magna aliquam erat volutpat. Ut wisi enim ad minim veniam, quis nostrud exerci tation ullamcorper suscipit lobortis nisl ut aliquip ex ea commodo consequat. Duis autem vel eum iriure dolor in hendrerit in vulputate velit esse molestie consequat.</p>
    </div>
    <div class="reviewer"><span class="avatar" role="img" aria-label="Portrait photo of the reviewer"></span>Mr. Owen Hartley</div>
  </section>
</section>

<footer class="site-footer">
  <div class="footer-col">
    <h5>Quick Links</h5>
    <ul><li>Home</li><li>About Us</li><li>Services</li><li>News</li><li>FAQs</li><li>Testimonials</li><li>Contact Us</li></ul>
  </div>
  <div class="footer-col">
    <h5>Contact Details</h5>
    <p>Phone<br>123-456-7890</p>
    <p>Address<br>Street Name Our Name<br>Town, Post Code</p>
    <p>Open Hours<br>Monday to Friday 9am–5pm</p>
  </div>
  <div class="footer-col enquiry">
    <h5>Quick Enquiry</h5>
    <p>Get a quote for your case today.<br>Fill in the form or phone us on 123-456-7890</p>
    <div class="enquiry-grid"><span></span><span></span><span></span><span></span><span class="wide"></span></div>
    <span class="btn-send">Call Me Back</span>
  </div>
  <div class="footer-brand">
    <span class="brand-mark"></span>
    <span class="brand-name">Brackwell<br>Counsel Partners</span>
  </div>
</footer>
<div class="copyright">Copyright © 2015 Brackwell Counsel Partners. All Rights Reserved.</div>

</body>
</html>
```